Lumara Health & Wellness Business Card Design

We would like to create business cards matching with our new logo design. The card should be professional looking but still have a playful side and something that would be eye catching. We are planing to open a luxury medical spa and looking to create a design based on this new logo. We are looking for a design that shows off luxury but not be gold in color. Also, while we are a more female oriented medical center we do have men that come in for our services and it should be be too feminine.

Target Market(s)

Health & Wellness. Medical patients. Luxury spa

Industry/Entity Type

Health And Wellness

Contact Information for Business Card

It should have the logo design in the front of card and back of card should have our contact information. Our current colors are peach/ coral, teal, and gray. We are looking for a modern looking design.

Font styles to use
Script

Colors
32a6d6
e667a6
86cfc6
fece3e

Requirements
Must have
• It should have our logo design. We would prefer to have a more modern look to the card.
Nice to have
• Eye-Catching Design on the personable side but still classy.
Should not have
• At this point we are looking for the best design. It should not have color purple.

```html
<!DOCTYPE html>
<html lang="en">
<head>
<meta charset="utf-8">
<title>Lumara Health &amp; Wellness – Business Card</title>
<link rel="stylesheet" href="https://fonts.googleapis.com/css2?family=Lato:ital,wght@0,300;0,400;1,700&display=swap">
<style>
  :root {
    --page-bg: #ffffff;
    --card-white: #ffffff;
    --marble-pink: #f9c0bc;
    --marble-blush: #fbd3cf;
    --marble-mist: #f4f3f2;
    --ink: #111111;
    --ink-soft: #3a3a3a;
    --card-shadow: rgba(0, 0, 0, 0.18);
  }
  * { box-sizing: border-box; margin: 0; padding: 0; }
  html, body {
    width: 1200px;
    height: 1200px;
    overflow: hidden;
    background: var(--page-bg);
  }
  .canvas {
    position: relative;
    width: 1200px;
    height: 1200px;
    font-family: "Lato", Arial, sans-serif;
  }
  .card {
    position: absolute;
    left: 260px;
    width: 680px;
    height: 378px;
    overflow: hidden;
    box-shadow: 0 4px 12px var(--card-shadow);
  }
  .card--front { top: 155px; }
  .card--back  { top: 665px; }

  .card__marble {
    position: absolute;
    inset: 0;
    background:
      radial-gradient(ellipse 60% 40% at 20% 30%, var(--marble-mist) 0%, transparent 70%),
      radial-gradient(ellipse 50% 35% at 80% 75%, var(--marble-mist) 0%, transparent 70%),
      radial-gradient(ellipse 70% 50% at 60% 20%, var(--marble-blush) 0%, transparent 75%),
      linear-gradient(135deg, var(--marble-pink) 0%, var(--marble-blush) 40%, var(--marble-pink) 70%, var(--marble-blush) 100%);
  }

  .card__panel {
    position: absolute;
    background: var(--card-white);
  }
  .card--front .card__panel {
    left: 33px;
    top: 33px;
    width: 615px;
    height: 315px;
    display: flex;
    align-items: center;
    justify-content: center;
  }
  .card--back .card__panel {
    left: 0;
    top: 85px;
    width: 580px;
    height: 215px;
    padding: 38px 0 0 28px;
  }

  .brand-name {
    font-family: "Lato", Arial, sans-serif;
    font-weight: 400;
    font-size: 38px;
    letter-spacing: 1px;
    color: var(--ink);
  }

  .contact__name {
    font-weight: 700;
    font-style: italic;
    font-size: 22px;
    letter-spacing: 0.5px;
    color: var(--ink);
    line-height: 1.15;
  }
  .contact__role {
    font-weight: 300;
    font-size: 18px;
    color: var(--ink-soft);
    margin-top: 4px;
    letter-spacing: 0.3px;
  }
  .contact__details {
    margin-top: 24px;
    font-weight: 300;
    font-size: 17px;
    color: var(--ink-soft);
    line-height: 1.35;
    letter-spacing: 0.3px;
    list-style: none;
  }
</style>
</head>
<body>
<main class="canvas">

  <section class="card card--front">
    <div class="card__marble" role="img" aria-label="Pink and white marbled paint pattern"></div>
    <div class="card__panel">
      <span class="brand-name">Lumara Health &amp; Wellness</span>
    </div>
  </section>

  <section class="card card--back">
    <div class="card__marble" role="img" aria-label="Pink and white marbled paint pattern"></div>
    <div class="card__panel">
      <p class="contact__name">MAREN CASTELL</p>
      <p class="contact__role">CO-FOUNDER</p>
      <ul class="contact__details">
        <li>EMAIL : marencastell@lumara.com</li>
        <li>PHONE : 555 014 2680</li>
      </ul>
    </div>
  </section>

</main>
</body>
</html>
```